Sports medicine multidisciplinary brochures

Multi-disciplinary sports medicine clinic. Need a range of pamphlet / foldable brochures to advertise our various services. Looking at keeping a similar 'look' between the various brochures to still ID as being part of the group, but perhaps slight colour variation / different front pic to distinguish them. Looking at a pamphlet for: 1) General clinic (about us) info 2) Concussion info 3) Podiatry 4) Sports Physicians 5) Exercise Physiology 6) Osteoarthritis 7) Physiotherapy. Modern feel, but still warm / inviting. See attached logo / cards / etc. Thank you!

Target Market(s)

Athletes, sports injuries + general health / medical

Industry/Entity Type

Clinic

Requirements
Nice to have
• Simple, warm design. Activity / health / lifestyle related feel.
• Design to allow easy adaptation of wording / content.

```html
<!DOCTYPE html>
<html lang="en">
<head>
<meta charset="utf-8">
<title>Riverside Sports &amp; Joint Clinic – Sports Physicians Brochure</title>
<link href="https://fonts.googleapis.com/css2?family=Jost:wght@400;500;600;700&family=Montserrat:wght@700;800&display=swap" rel="stylesheet">
<style>
:root{
  --bg:#e4e4e4;
  --paper:#ffffff;
  --orange:#f07a1a;
  --orange-deep:#e8561c;
  --amber:#f7a51c;
  --tan:#e9a456;
  --peach:#fbd7b5;
  --peach-soft:#fde9d6;
  --butter:#fdf0b8;
  --red:#e2231a;
  --green:#2f9e55;
  --ink:#4a4a4a;
  --ink-soft:#6d6d6d;
}
*{box-sizing:border-box;margin:0;padding:0}
html,body{width:1200px;height:899px;overflow:hidden;background:var(--bg)}
body{position:relative;font-family:"Jost",sans-serif;color:var(--ink)}
.spread{position:absolute;width:580px;height:410px;display:flex;background:var(--paper);box-shadow:0 6px 18px rgba(0,0,0,.18)}
.spread--inside{left:30px;top:30px}
.spread--outside{left:590px;top:459px}
.page{position:relative;width:290px;height:410px;overflow:hidden}
.page + .page{border-left:1px solid #eee}
.photo{position:absolute}
svg.shape{position:absolute;left:0;top:0}
.heading{font-family:"Montserrat",sans-serif;font-weight:800;color:var(--red);font-size:8.6px;line-height:1.2}
.body-text{font-size:6px;line-height:1.45;color:var(--ink)}
.bullets{list-style:none;font-size:5.6px;line-height:1.55}
.bullets li::before{content:"•";color:var(--red);margin-right:3px}
.pill{border-radius:8px;padding:5px 8px}

/* inside left */
.team-title{position:absolute;left:16px;top:128px;font-family:"Jost",sans-serif;font-weight:500;font-size:24px;color:#fff;letter-spacing:.5px}
.team-list{position:absolute;left:16px;top:160px;display:flex;gap:14px;font-size:5.4px;line-height:1.4;color:#fff}
.team-list b{display:block;font-size:6px}
.intro{position:absolute;left:16px;top:228px;width:258px}
.intro .heading{margin:8px 0 4px}

/* inside right */
.qa{position:absolute;left:14px;width:262px}
.qa .heading{margin-bottom:4px}
.qa--one{top:128px}
.qa--two{top:272px}
.box-peach{background:var(--peach);margin-top:4px}
.box-butter{background:var(--butter);margin-top:4px}

/* outside back */
.back-block{position:absolute;left:16px;width:258px}
.back-block--competency{top:22px}
.back-block--athletes{top:128px}
.contact{position:absolute;left:16px;top:190px;width:258px}
.contact-intro{font-size:5.8px;color:var(--ink-soft)}
.contact-label{font-size:7px;font-weight:600;margin-top:4px}
.hours-title{font-family:"Montserrat",sans-serif;font-weight:800;font-size:8px;color:var(--red);margin-top:6px}
.hours{border-collapse:collapse;font-size:6.6px;margin-top:2px}
.hours td{padding:1px 18px 1px 0;border-bottom:1px solid #ddd}
.details{position:absolute;left:144px;top:312px;width:140px}
.clinic-name{font-family:"Montserrat",sans-serif;font-weight:700;font-size:7px;color:var(--red)}
.address{font-size:6.2px;margin-top:1px}
.phone{font-size:11px;font-weight:700;color:#222;margin-top:1px}
.web{font-size:5.8px;color:var(--ink-soft);line-height:1.4;margin-top:1px}
.map{position:absolute;left:16px;top:314px;width:120px;height:64px;background:linear-gradient(135deg,#eceff2,#d9dee3);border:2px solid var(--tan)}
.foot-bar{position:absolute;left:0;bottom:0;width:100%;height:10px;background:var(--orange)}

/* outside front */
.brand{position:absolute;left:36px;top:48px;display:flex;align-items:center;gap:6px;font-family:"Montserrat",sans-serif;font-weight:800;font-size:20px;color:var(--green);letter-spacing:1px}
.brand-dot{width:12px;height:12px;border-radius:50%;background:var(--orange)}
.brand-sub{position:absolute;left:56px;top:74px;font-size:5px;letter-spacing:1px;color:var(--orange)}
.cover-title{position:absolute;left:70px;top:212px;width:210px;text-align:right;color:#fff;font-family:"Montserrat",sans-serif;font-weight:800;font-size:16px;line-height:1.1}
.cover-sub{position:absolute;left:70px;top:254px;width:210px;text-align:right;color:#fff;font-size:10px;line-height:1.25}
</style>
</head>
<body>

<section class="spread spread--inside">
  <article class="page page--team">
    <div class="photo" role="img" aria-label="Cyclist riding on an open road" style="left:0;top:0;width:290px;height:130px;background:linear-gradient(160deg,#5d6f88,#8ea3b5 55%,#b9c4b2)"></div>
    <svg class="shape" width="290" height="410" viewBox="0 0 290 410" aria-hidden="true">
      <path d="M0 118 C70 92 120 140 190 112 C230 96 262 86 290 92 L290 210 C230 230 160 196 90 220 C50 232 20 228 0 222 Z" fill="var(--tan)"/>
      <path d="M0 222 C40 232 110 214 170 216 C220 218 260 228 290 210 L290 230 C230 246 160 226 90 238 C50 244 20 240 0 236 Z" fill="var(--peach)"/>
      <path d="M150 0 C190 40 230 60 290 52 L290 0 Z" fill="var(--orange)" opacity=".85"/>
      <path d="M0 300 C60 320 80 380 40 410 L0 410 Z" fill="var(--peach-soft)"/>
    </svg>
    <h2 class="team-title">PHYSICIANS</h2>
    <div class="team-list">
      <p><b>Dr Liam Harcourt</b>BA, MBBS, FASMC<br>Sport &amp; Exercise Physician</p>
      <p><b>Dr Owen Marsh</b>MBBS, FASMC<br>Sport &amp; Exercise Physician</p>
      <p><b>Dr Paul Benning</b>MBBS, PhD, FASMC<br>Sport &amp; Exercise Physician</p>
    </div>
    <div class="intro">
      <p class="body-text">The Riverside Sports &amp; Joint Clinic is a new multidisciplinary clinic with specialist sport and exercise physicians at the lead. We aim to provide affordable, evidence based, non-surgical treatment for all sporting and musculoskeletal injuries, as well as osteoarthritis. Combining specialist physicians with physiotherapy, podiatry, exercise physiology and other allied health disciplines under one roof, we are uniquely placed to work with you.</p>
      <h3 class="heading">What is a Sports Physician specialist?</h3>
      <p class="body-text">Sport and Exercise Physicians are medical specialists with extensive training in the management of musculoskeletal injuries and medical problems affecting active people. They work with people of all ages and abilities, from the weekend walker to elite athletes, providing a complete plan of care and working alongside your general practitioner.</p>
    </div>
  </article>

  <article class="page page--roles">
    <div class="photo" role="img" aria-label="Swimmer in a yellow cap doing freestyle in a pool" style="left:0;top:0;width:290px;height:120px;background:linear-gradient(180deg,#2a6fb8,#4ea3d8 60%,#8fcbea)"></div>
    <svg class="shape" width="290" height="410" viewBox="0 0 290 410" aria-hidden="true">
      <path d="M0 96 C60 130 120 100 180 108 C230 114 260 128 290 112 L290 130 C240 142 200 124 150 122 C90 120 40 140 0 118 Z" fill="var(--orange)"/>
      <path d="M0 118 C40 140 90 120 150 122 C200 124 240 142 290 130 L290 140 L0 140 Z" fill="var(--paper)"/>
    </svg>
    <div class="qa qa--one">
      <h3 class="heading">What is the difference between a sports physician and an orthopaedic surgeon?</h3>
      <p class="body-text">Both are well trained in musculoskeletal medicine, but sports physicians specialise in non-operative care while surgeons specialise in operations. Around 90% of injuries are non-surgical, so the physician can tailor treatment, guide rehab and refer on when needed.</p>
      <ul class="bullets pill box-peach">
        <li>Concussion and other head injuries</li>
        <li>Diagnostic and interventional use of ultrasound to guide treatment</li>
        <li>Athletes with acute or chronic illness (including diabetes, asthma)</li>
        <li>Nutrition, supplements and performance optimisation</li>
        <li>Exercise prescription for those wanting to increase their fitness</li>
        <li>Injury prevention</li>
        <li>"Return to play" decisions</li>
        <li>Healthy lifestyle promotion</li>
      </ul>
    </div>
    <div class="qa qa--two">
      <h3 class="heading">ASMC fellows often act as the primary contact for elite sports teams and athletes:</h3>
      <ul class="bullets pill box-butter">
        <li>Assessing and diagnosing injuries or illness</li>
        <li>Close integration with the team and its training demands</li>
        <li>Devising and coordinating a full management program</li>
        <li>Understanding drug testing in elite settings and high demand athletes</li>
        <li>Making sure your injury is corrected and you stay playing your sport</li>
      </ul>
    </div>
  </article>
</section>

<section class="spread spread--outside">
  <article class="page page--back">
    <svg class="shape" width="290" height="410" viewBox="0 0 290 410" aria-hidden="true">
      <path d="M0 40 C80 0 180 10 290 0 L290 70 C200 60 120 100 0 120 Z" fill="var(--peach)"/>
    </svg>
    <div class="back-block back-block--competency">
      <h3 class="heading">ASMC fellows also have extensive competency in "exercise is medicine"</h3>
      <ul class="bullets" style="margin-top:4px">
        <li>Management of lifestyle diseases such as diabetes and heart disease</li>
        <li>Non-surgical management of tendon and joint injuries</li>
        <li>Dive and altitude medicine</li>
        <li>Medical screenings and health assessments including ECGs</li>
        <li>Travel medicine and vaccinations</li>
      </ul>
    </div>
    <div class="back-block back-block--athletes">
      <h3 class="heading">Do Sports Physicians only treat competitive athletes?</h3>
      <p class="body-text" style="margin-top:3px">No, our specialists are ideal for anyone who wants to stay active, return to work or begin an exercise program. A referral from your GP is recommended but not needed to book a visit with our physicians.</p>
    </div>
    <div class="contact">
      <p class="contact-intro">For more information or to book an appointment with one of our services,</p>
      <p class="contact-label">Please Contact</p>
      <p class="hours-title">OPENING HOURS</p>
      <table class="hours">
        <tr><td>Monday - Wednesday</td><td>8:30 - 6</td></tr>
        <tr><td>Thursday</td><td>8:30 - 8</td></tr>
        <tr><td>Friday</td><td>8:30 - 3</td></tr>
        <tr><td>Saturday</td><td>9 - 12:30</td></tr>
      </table>
    </div>
    <div class="map" role="img" aria-label="Street map showing the clinic location"></div>
    <div class="details">
      <p class="clinic-name">Riverside Sports &amp; Joint Clinic</p>
      <p class="address">14 Harbour Lane, Westvale, SA 5099</p>
      <p class="phone">(08) 5550 1420</p>
      <p class="web">hello@riversidesportsclinic.example<br>www.riversidesportsclinic.example<br>ABN 12 345 678 901</p>
    </div>
    <div class="foot-bar"></div>
  </article>

  <article class="page page--cover">
    <svg class="shape" width="290" height="410" viewBox="0 0 290 410" aria-hidden="true">
      <defs>
        <linearGradient id="coverFlow" x1="0" y1="0" x2="1" y2="1">
          <stop offset="0" stop-color="var(--amber)"/>
          <stop offset="1" stop-color="var(--orange-deep)"/>
        </linearGradient>
      </defs>
      <path d="M120 0 L290 0 L290 410 L150 410 C230 340 120 280 190 200 C240 140 180 70 120 0 Z" fill="url(#coverFlow)" opacity=".75"/>
      <path d="M40 170 C120 150 200 190 290 160 L290 410 L160 410 C200 360 140 330 90 300 C50 270 30 220 40 170 Z" fill="url(#coverFlow)"/>
      <path d="M0 396 C100 404 200 396 290 380 L290 410 L0 410 Z" fill="var(--orange)"/>
    </svg>
    <div class="brand"><span class="brand-dot"></span>KINETA</div>
    <p class="brand-sub">SPORTS &amp; JOINT CLINIC</p>
    <h1 class="cover-title">THE RIVERSIDE SPORTS &amp; JOINT CLINIC</h1>
    <p class="cover-sub">is a new multidisciplinary clinic with specialist sports &amp; exercise physicians as the leads</p>
  </article>
</section>

</body>
</html>
```